BOLD & MINIMALIST DESIGN NEEDED

We want a very bold but minimalistic business card design that is impactful and utilizes both sides of the business card. Our current logo is included for your use.

We want bold fonts and good use of negative space. We don't want the logo to overpower the design.

Target Market(s)

Professionals who are building new commercial buildings.

Industry/Entity Type

Construction

Contact Information for Business Card

Name, Title, email, office phone, cell phone, website

Font styles to use
Serif
Sans Serif

Requirements
Must have
• Bold design!

```html
<!DOCTYPE html>
<html lang="en">
<head>
<meta charset="utf-8">
<title>Summitline Build – Business Card</title>
<link rel="stylesheet" href="https://fonts.googleapis.com/css2?family=Archivo+Black&family=Archivo:wght@700;800&display=swap">
<style>
  :root {
    --backdrop: #2e2e2e;
    --card-white: #ffffff;
    --ink: #1b1a1d;
    --brand-green: #7bbd24;
    --card-shadow: rgba(0, 0, 0, 0.45);
  }
  * { margin: 0; padding: 0; box-sizing: border-box; }
  html, body {
    width: 1200px;
    height: 900px;
    overflow: hidden;
    background: var(--backdrop);
  }
  .canvas {
    position: relative;
    width: 1200px;
    height: 900px;
  }
  .card {
    position: absolute;
    left: 280px;
    width: 640px;
    height: 366px;
    background: var(--card-white);
    box-shadow: 0 10px 28px var(--card-shadow);
    overflow: hidden;
  }
  .card--front { top: 46px; }
  .card--back { top: 460px; }

  /* Front */
  .brand {
    position: absolute;
    inset: 0;
    display: flex;
    align-items: center;
    justify-content: center;
    gap: 16px;
  }
  .brand__mark {
    width: 30px;
    height: 30px;
    background: var(--brand-green);
  }
  .brand__name {
    font-family: "Archivo Black", "Arial Black", sans-serif;
    font-size: 46px;
    letter-spacing: 0.5px;
    color: var(--ink);
  }

  /* Back */
  .back__band {
    position: absolute;
    left: 0;
    top: 0;
    width: 205px;
    height: 100%;
    background: var(--ink);
  }
  .holder {
    position: absolute;
    left: 240px;
    top: 46px;
  }
  .holder__name {
    font-family: "Archivo Black", "Arial Black", sans-serif;
    font-size: 40px;
    line-height: 0.9;
    color: var(--brand-green);
    text-transform: uppercase;
  }
  .holder__title {
    margin-top: 8px;
    font-family: "Archivo", Arial, sans-serif;
    font-weight: 800;
    font-size: 14px;
    letter-spacing: 0.3px;
    color: var(--ink);
    text-transform: uppercase;
  }
  .contact {
    position: absolute;
    left: 240px;
    top: 186px;
  }
  .contact__phones {
    font-family: "Archivo Black", "Arial Black", sans-serif;
    font-size: 35px;
    line-height: 1;
    color: var(--ink);
    letter-spacing: 1px;
  }
  .contact__online {
    margin-top: 26px;
    font-family: "Archivo", Arial, sans-serif;
    font-weight: 800;
    font-size: 15px;
    line-height: 1.3;
    letter-spacing: 0.6px;
    text-transform: uppercase;
  }
  .contact__email { color: var(--ink); }
  .contact__web { color: var(--brand-green); }
</style>
</head>
<body>
<main class="canvas">
  <section class="card card--front" aria-label="Card front">
    <div class="brand">
      <span class="brand__mark"></span>
      <span class="brand__name">SUMMITLINE BUILD</span>
    </div>
  </section>

  <section class="card card--back" aria-label="Card back">
    <div class="back__band"></div>
    <div class="holder">
      <h1 class="holder__name">Marcus<br>Delaney</h1>
      <p class="holder__title">Managing Director</p>
    </div>
    <div class="contact">
      <p class="contact__phones">204 0142 3087<br>204 0199 4620</p>
      <p class="contact__online">
        <span class="contact__email">info@summitlinebuild.com</span><br>
        <span class="contact__web">www.summitlinebuild.com</span>
      </p>
    </div>
  </section>
</main>
</body>
</html>
```